Course Graduation Certificate

This project is not for a flyer but instead for the creation of a course graduation certificate. The final certificate needs to include the Marlowe Summit Aviation Academy logo and the text stating as follows:
Certifies that ___________________________ has satisfactorily completed the course of _______________________________ on ________________________________
I would also like to include some type of gold seal of completion as well as a place to sign my name and credentials at the bottom of the certificate
I have included the Marlowe Summit Aviation Academy logo as well as three other certificate examples for you to work from.
Target Market(s)
Students completing a certification course and receiving a certificate
Look and feel

```html
<!DOCTYPE html>
<html lang="en">
<head>
<meta charset="utf-8">
<title>Course Graduation Certificate</title>
<link href="https://fonts.googleapis.com/css2?family=Cinzel:wght@500;600&family=Pinyon+Script&display=swap" rel="stylesheet">
<style>
  :root {
    --backdrop: #d5d3cf;
    --paper: #ffffff;
    --field: #f3f7fc;
    --field-edge: #e3ecf7;
    --cobalt: #0a62b0;
    --gold-light: #f3de86;
    --gold: #d2ab4e;
    --gold-deep: #8f6a1f;
    --ink: #1a1a1a;
    --rule: #d9b35c;
  }
  * { margin: 0; padding: 0; box-sizing: border-box; }
  html, body {
    width: 1200px;
    height: 800px;
    overflow: hidden;
    background: var(--backdrop);
  }
  .certificate {
    position: absolute;
    left: 100px;
    top: 14px;
    width: 1000px;
    height: 772px;
    background: var(--paper);
    font-family: "Cinzel", serif;
  }
  .certificate__field {
    position: absolute;
    left: 43px;
    top: 43px;
    width: 913px;
    height: 687px;
    background: radial-gradient(ellipse at center, var(--field) 40%, var(--field-edge) 100%);
  }
  .certificate__art {
    position: absolute;
    inset: 0;
    width: 1000px;
    height: 772px;
  }
  .certificate__title {
    position: absolute;
    left: 0;
    width: 1000px;
    top: 58px;
    text-align: center;
    font-family: "Pinyon Script", cursive;
    font-size: 112px;
    line-height: 1.2;
    color: var(--cobalt);
    text-shadow: 2px 4px 5px rgba(0, 0, 0, 0.18);
  }
  .certificate__line-text {
    position: absolute;
    left: 0;
    width: 1000px;
    text-align: center;
    font-size: 15px;
    font-weight: 600;
    letter-spacing: 1.6px;
    text-transform: uppercase;
    color: var(--ink);
  }
  .certificate__line-text--certifies { top: 240px; }
  .certificate__line-text--course { top: 362px; font-size: 13.5px; }
  .certificate__conferred {
    position: absolute;
    left: 320px;
    top: 507px;
    font-size: 15px;
    font-weight: 600;
    letter-spacing: 1.6px;
    text-transform: uppercase;
    color: var(--ink);
  }
  .certificate__academy {
    position: absolute;
    left: 378px;
    top: 622px;
    width: 260px;
    text-align: center;
    font-size: 17px;
    font-weight: 600;
    line-height: 1.25;
    letter-spacing: 0.5px;
    color: var(--cobalt);
  }
  .certificate__signature-label {
    position: absolute;
    left: 716px;
    width: 163px;
    top: 655px;
    text-align: center;
    font-size: 12px;
    font-weight: 600;
    letter-spacing: 1.4px;
    text-transform: uppercase;
    color: var(--cobalt);
  }
</style>
</head>
<body>
  <main class="certificate">
    <div class="certificate__field" role="img" aria-label="Fine blue guilloche security pattern background"></div>

    <svg class="certificate__art" viewBox="0 0 1000 772" aria-hidden="true">
      <defs>
        <linearGradient id="goldBand" x1="0" y1="0" x2="1" y2="1">
          <stop offset="0" stop-color="var(--gold-light)"/>
          <stop offset="0.55" stop-color="var(--gold)"/>
          <stop offset="1" stop-color="var(--gold-deep)"/>
        </linearGradient>
        <radialGradient id="sealGold" cx="0.4" cy="0.35" r="0.7">
          <stop offset="0" stop-color="#fbe9a6"/>
          <stop offset="0.6" stop-color="#d9b04f"/>
          <stop offset="1" stop-color="#9a7224"/>
        </radialGradient>
      </defs>

      <!-- frames -->
      <rect class="frame-gold" x="43" y="43" width="913" height="687" fill="none" stroke="var(--rule)" stroke-width="1.2"/>
      <path class="frame-blue" d="M147 35 H964 V640 M861 737 H36 V159" fill="none" stroke="var(--cobalt)" stroke-width="2.5"/>

      <!-- writing rules -->
      <line x1="132" y1="321" x2="868" y2="321" stroke="var(--rule)" stroke-width="1.2"/>
      <line x1="132" y1="441" x2="868" y2="441" stroke="var(--rule)" stroke-width="1.2"/>
      <line x1="469" y1="522" x2="682" y2="522" stroke="var(--rule)" stroke-width="1"/>
      <line x1="716" y1="649" x2="879" y2="649" stroke="var(--rule)" stroke-width="1"/>

      <!-- corner ribbons -->
      <g class="ribbon ribbon--top-left">
        <polygon points="0,97 96,0 175,0 0,175" fill="var(--cobalt)"/>
        <polygon points="0,159 69,91 106,91 0,197" fill="url(#goldBand)"/>
        <line x1="47" y1="35" x2="90" y2="0" stroke="#111" stroke-width="4"/>
      </g>
      <g class="ribbon ribbon--bottom-right">
        <polygon points="823,772 907,772 1000,680 1000,605" fill="var(--cobalt)"/>
        <polygon points="894,681 930,681 1000,612 1000,576" fill="url(#goldBand)"/>
        <line x1="911" y1="772" x2="951" y2="739" stroke="#111" stroke-width="4"/>
      </g>

      <!-- seal of completion -->
      <circle class="seal" cx="154" cy="636" r="54" fill="url(#sealGold)"/>
    </svg>

    <h1 class="certificate__title">Certificate</h1>
    <p class="certificate__line-text certificate__line-text--certifies">Certifies that</p>
    <p class="certificate__line-text certificate__line-text--course">has satisfactorily completed the course of</p>
    <p class="certificate__conferred">Conferred on</p>
    <p class="certificate__academy">Marlowe Summit<br>Aviation Academy</p>
    <p class="certificate__signature-label">Signature</p>
  </main>
</body>
</html>
```